Veltrix4 Business Card - Health

Veltrix4 maximizes value from the health data of its clients, including doctors, HMOs, and patients. I have attached the Veltrix4 logo as an ai and eps file.
Target Market(s)
Health, HMO, Healthcare, Data, Big Data, Data Analytics
Industry/Entity Type
Business
Requirements
Must have
- At least one side should have some white on it so that we can write on it.

```html
<!DOCTYPE html>
<html lang="en">
<head>
<meta charset="utf-8">
<title>Veltrix4 Business Card</title>
<link rel="stylesheet" href="https://fonts.googleapis.com/css2?family=Poppins:wght@300&family=Open+Sans:wght@400;700&family=Roboto+Condensed:wght@400&display=swap">
<style>
  :root {
    --backdrop: #e6e6e8;
    --card: #121315;
    --card-edge: #1b1c1f;
    --ink: #ffffff;
    --muted: #c9cbd0;
    --accent: #1f8fea;
    --silver: #d9dadd;
    --write: #ffffff;
  }
  * { margin: 0; padding: 0; box-sizing: border-box; }
  html, body { width: 1200px; height: 1200px; overflow: hidden; }
  body {
    background: var(--backdrop);
    position: relative;
    font-family: "Open Sans", sans-serif;
  }
  .card {
    position: absolute;
    left: 250px;
    width: 700px;
    height: 400px;
    border-radius: 24px;
    background: linear-gradient(120deg, var(--card-edge), var(--card) 60%);
    overflow: hidden;
    box-shadow: 0 6px 18px rgba(0,0,0,0.18);
  }
  .card--front { top: 150px; }
  .card--back { top: 640px; }

  .brand {
    position: absolute;
    display: flex;
    align-items: center;
    gap: 22px;
  }
  .brand__dot {
    border-radius: 50%;
    background: var(--accent);
  }
  .brand__name {
    font-family: "Poppins", sans-serif;
    font-weight: 300;
    color: var(--ink);
    letter-spacing: 1px;
  }
  .card--front .brand { left: 50%; top: 50%; transform: translate(-50%, -50%); }
  .card--front .brand__dot { width: 72px; height: 72px; }
  .card--front .brand__name { font-size: 78px; line-height: 1; }

  .card--back .brand { right: 42px; top: 36px; gap: 14px; }
  .card--back .brand__dot { width: 46px; height: 46px; }
  .card--back .brand__name { font-size: 50px; line-height: 1; }

  .frame { position: absolute; left: 0; top: 0; }

  .contact {
    position: absolute;
    right: 42px;
    top: 148px;
    text-align: right;
    color: var(--ink);
  }
  .contact__name { font-weight: 700; font-size: 22px; line-height: 1.1; }
  .contact__role { font-size: 13px; color: var(--muted); margin-bottom: 18px; }
  .contact__list {
    list-style: none;
    font-family: "Roboto Condensed", sans-serif;
    font-size: 16px;
    line-height: 27px;
  }
  .contact__list li { display: flex; justify-content: flex-end; align-items: center; gap: 10px; }
  .contact__icon { width: 15px; height: 15px; flex: none; }
  .contact__icon--none { width: 15px; }
</style>
</head>
<body>
  <section class="card card--front" aria-label="Card front">
    <div class="brand">
      <span class="brand__dot"></span>
      <span class="brand__name">Veltrix4</span>
    </div>
  </section>

  <section class="card card--back" aria-label="Card back">
    <svg class="frame" width="700" height="400" viewBox="0 0 700 400" aria-hidden="true">
      <polygon points="150,70 330,210 170,390 -10,250" fill="none" stroke="var(--accent)" stroke-width="5"/>
      <polygon points="165,90 310,210 175,365 20,245" fill="none" stroke="var(--silver)" stroke-width="4"/>
      <polygon class="frame__write" points="180,112 290,210 180,340 50,240" fill="var(--write)" stroke="var(--accent)" stroke-width="3"/>
    </svg>

    <div class="brand">
      <span class="brand__dot"></span>
      <span class="brand__name">Veltrix4</span>
    </div>

    <div class="contact">
      <p class="contact__name">Your Long Name</p>
      <p class="contact__role">Director</p>
      <ul class="contact__list">
        <li>+00 111 222 3333
          <svg class="contact__icon" viewBox="0 0 16 16" aria-hidden="true"><path d="M4 1l3 3-2 2c1 2 3 4 5 5l2-2 3 3-2 3C7 15 1 9 1 3z" fill="var(--accent)"/></svg>
        </li>
        <li>yourname@yourwebsite.com
          <svg class="contact__icon" viewBox="0 0 16 16" aria-hidden="true"><circle cx="8" cy="8" r="7" fill="var(--accent)"/><path d="M1 8h14M8 1c-3 4-3 10 0 14M8 1c3 4 3 10 0 14" fill="none" stroke="var(--card)" stroke-width="1.2"/></svg>
        </li>
        <li>www.yourwebsite.com
          <svg class="contact__icon" viewBox="0 0 16 16" aria-hidden="true"><rect x="1" y="3" width="14" height="10" rx="1" fill="var(--accent)"/><path d="M1 4l7 5 7-5" fill="none" stroke="var(--card)" stroke-width="1.4"/></svg>
        </li>
        <li>12 Harlow Lane, Brookvale, NT, 0840
          <span class="contact__icon contact__icon--none"></span>
        </li>
      </ul>
    </div>
  </section>
</body>
</html>
```